Retail Package for Ammunition Company

We are looking for a packaging design for a retail boxed ammunition. The "look". Attached will be logo to be used. Box to represent strength and accuracy. Will need to provide .psd files to allow in house person to add/remove text to other calibers and warnings.

Browse Other Brands: http://www.brightcartridge.example/brands

The packaging needs to include:
Logo- provided and the following text:

FRONT 1. 9mm 115gr FMJ

BACK 2. WARNING: To avoid serious injury: (1) use only ammunition in good condition; use only in modern firearms in good condition marked for .22 Long Rifle (LR) cartridges; (2) always be sure barrel is free of any obstructions; the barrel should be checked in case of light recoil, or an unusually loud or weak sound heard during firing; (3) wear eye and ear protection; (4) if gun fails to fire, avoid exposure to breech when unloading and point muzzle in a safe direction. Keep firearm pointed in safe direction at all times; (5) discharge may occur if rim is struck; handle with caution, do not drop. (6) Do not shoot at hard surfaces or water to prevent ricochet; (7) Bullet is capable of traveling extreme distances. Know your backstop; (8) Store in cool dry place

3. LEAD WARNING: Discharging firearms in poorly ventilated areas, cleaning firearms, or handling ammunition may result in exposure to lead and other substances known to cause birth defects, reproductive harm, and other serious physical injury. Have adequate ventilation at all times. Wash hands thoroughly after exposure.

Dimensions ; (LxWxH): 5.25" x 2.625" x 1.125"

Target Market(s)

US Veterans, Gun and Ammo enthusiast. Military/Law Enforcement person.

Industry/Entity Type

Gun

Requirements
Must have
• Logo provided, text provided
Nice to have
• would like to see a package that looks better than the leaders, such as Halvorsen, TWP, Brackenford, Meltaro. .....just browse these brands: http://www.brightcartridge.example/brands
Should not have
• cartoonist style characters. No animals.

```html
<!DOCTYPE html>
<html lang="en">
<head>
<meta charset="utf-8">
<title>Bulwark Rounds – Retail Box Dieline</title>
<link rel="stylesheet" href="https://fonts.googleapis.com/css2?family=Montserrat:wght@800&family=Roboto+Condensed:wght@400;700&display=swap">
<style>
  :root {
    --canvas-grey: #d3d3d3;
    --box-navy: #1f3768;
    --ink-white: #ffffff;
    --warning-orange: #e4572e;
    --placeholder-warm: #b89a5c;
    --placeholder-soft: #a88d55;
  }
  * { margin: 0; padding: 0; box-sizing: border-box; }
  html, body { width: 1200px; height: 600px; overflow: hidden; }
  body { background: var(--canvas-grey); }
  .dieline { position: relative; width: 1200px; height: 600px; }
  .dieline-shapes { position: absolute; inset: 0; }
  .dieline-shapes .panel { fill: var(--box-navy); }

  .brand-name {
    position: absolute;
    color: var(--ink-white);
    font-family: "Montserrat", sans-serif;
    font-weight: 800;
    text-align: center;
    line-height: 1;
  }
  .brand-name .word-main { display: block; }
  .brand-name .word-sub { display: block; letter-spacing: 0.42em; }

  .front-brand { left: 210px; top: 214px; width: 360px; }
  .front-brand .word-main { font-size: 52px; letter-spacing: 0.01em; }
  .front-brand .word-sub { font-size: 17px; margin-top: 6px; margin-left: 0.42em; }

  .top-flap-brand { left: 240px; top: 124px; width: 300px; transform: rotate(180deg); }
  .top-flap-brand .word-main { font-size: 36px; }
  .top-flap-brand .word-sub { font-size: 12px; margin-top: 5px; margin-left: 0.42em; }

  .side-brand { width: 170px; transform: rotate(-90deg); transform-origin: center; }
  .side-brand .word-main { font-size: 30px; }
  .side-brand .word-sub { font-size: 10px; margin-top: 4px; margin-left: 0.42em; }
  .side-brand.left { left: 63px; top: 278px; }
  .side-brand.right { left: 539px; top: 278px; }

  .cartridge-image {
    position: absolute;
    left: 232px; top: 308px; width: 314px; height: 44px;
    background: linear-gradient(90deg, var(--placeholder-soft), var(--placeholder-warm));
  }

  .product-line {
    position: absolute;
    left: 190px; top: 368px; width: 394px;
    text-align: center;
    color: var(--ink-white);
    font-family: "Roboto Condensed", sans-serif;
    font-weight: 700;
    font-size: 16px;
    letter-spacing: 0.12em;
    line-height: 1;
  }

  .back-warnings {
    position: absolute;
    left: 685px; top: 214px; width: 408px;
    color: var(--ink-white);
    font-family: "Roboto Condensed", sans-serif;
    font-size: 8.6px;
    line-height: 1.5;
  }
  .back-warnings p + p { margin-top: 10px; }
  .warning-tag {
    background: var(--warning-orange);
    font-weight: 700;
    padding: 0 2px;
  }
</style>
</head>
<body>
<main class="dieline">
  <svg class="dieline-shapes" width="1200" height="600" viewBox="0 0 1200 600" aria-hidden="true">
    <defs>
      <filter id="panel-shadow" x="-10%" y="-10%" width="120%" height="130%">
        <feDropShadow dx="4" dy="6" stdDeviation="4" flood-color="#000" flood-opacity="0.35"/>
      </filter>
    </defs>
    <g filter="url(#panel-shadow)">
      <path class="panel top-flap" d="M190,196 V84 Q190,68 206,68 H567 Q583,68 583,84 V196 Z"/>
      <path class="panel left-tuck-top" d="M190,110 H117 L110,118 V196 H190 Z"/>
      <path class="panel left-side" d="M105,195 H191 V406 H105 Z"/>
      <path class="panel left-tuck-bottom" d="M105,405 L110,476 H190 V405 Z"/>
      <path class="panel front" d="M190,195 H584 V406 H190 Z"/>
      <path class="panel front-lip" d="M192,405 Q198,420 214,420 H560 Q576,420 580,405 Z"/>
      <path class="panel right-tuck-top" d="M583,110 H656 L662,118 V196 H583 Z"/>
      <path class="panel right-side" d="M583,195 H666 V406 H583 Z"/>
      <path class="panel right-tuck-bottom" d="M583,405 V476 H660 L666,405 Z"/>
      <path class="panel back" d="M665,195 H1105 V406 H665 Z"/>
      <path class="panel back-flap" d="M665,405 V504 Q665,520 681,520 H1044 Q1060,520 1060,504 V405 Z"/>
    </g>
  </svg>

  <div class="brand-name top-flap-brand">
    <span class="word-main">BULWARK</span>
    <span class="word-sub">ROUNDS</span>
  </div>

  <div class="brand-name side-brand left">
    <span class="word-main">BULWARK</span>
    <span class="word-sub">ROUNDS</span>
  </div>

  <div class="brand-name front-brand">
    <span class="word-main">BULWARK</span>
    <span class="word-sub">ROUNDS</span>
  </div>

  <div class="cartridge-image" role="img" aria-label="Photograph of a brass rifle cartridge with a copper bullet, lying horizontally"></div>

  <p class="product-line">9mm 115gr FMJ</p>

  <div class="brand-name side-brand right">
    <span class="word-main">BULWARK</span>
    <span class="word-sub">ROUNDS</span>
  </div>

  <section class="back-warnings">
    <p><span class="warning-tag">WARNING :</span> To avoid serious injury: (1) use only ammunition in good condition; use only in modern firearms in good condition marked for .22 Long Rifle (LR) cartridges; (2) always be sure barrel is free of any obstructions; the barrel should be checked in case of light recoil, or an unusually loud or weak sound heard during firing; (3) wear eye and ear protection; (4) if gun fails to fire, avoid exposure to breech when unloading and point muzzle in a safe direction. Keep firearm pointed in safe direction at all times; (5) discharge may occur if rim is struck; handle with caution, do not drop. (6) Do not shoot at hard surfaces or water to prevent ricochet; (7) Bullet is capable of traveling extreme distances. Know your backstop; (8) Store in cool dry place.</p>
    <p><span class="warning-tag">LEAD WARNING :</span> Discharging firearms in poorly ventilated areas, cleaning firearms, or handling ammunition may result in exposure to lead and other substances known to cause birth defects, reproductive harm, and other serious physical injury. Have adequate ventilation at all times. Wash hands thoroughly after exposure.</p>
  </section>
</main>
</body>
</html>
```